Digital Menu Board for Restaurant

I want a digital menu board for our new restaurant. I have provided the sample of what I kind of want.
This is to be on a 55 inch tv so it needs to be the correct aspect ratio of 4:5

Font styles to use
Serif
Sans Serif

Colors
f59296
f04a50
ec1f27
ffffff
fffef7
fbed22
ffc214
0592cd
e5519f

Requirements
Must have
• fun, maybe something moving? bright colors on a darker background so it's easy to read or dark font on a light background.

```html
<!DOCTYPE html>
<html lang="en">
<head>
<meta charset="utf-8">
<title>Sand Dollar Menu Board</title>
<link rel="stylesheet" href="https://fonts.googleapis.com/css2?family=Caveat+Brush&family=Patrick+Hand&display=swap">
<style>
:root{
  --page:#ffffff;
  --board:#2a2a2a;
  --buns:#0d90cd;
  --shore:#9fc54a;
  --sides:#efbd32;
  --drinks:#d0539a;
  --shakes:#d44e52;
  --kids:#64a6d4;
  --brand:#e0582a;
  --ink:#fffef7;
  --dark:#1c1c1c;
  --accent-yellow:#fbed22;
  --accent-pink:#e5519f;
  --accent-coral:#f59296;
}
*{margin:0;padding:0;box-sizing:border-box}
html,body{width:1000px;height:1200px;overflow:hidden;background:var(--page)}
.canvas{position:relative;width:1000px;height:1200px;font-family:"Patrick Hand",sans-serif;color:var(--ink)}
.board{position:absolute;left:100px;top:100px;width:800px;height:1000px;background:var(--board)}
.panels{position:absolute;left:0;top:0}
.block{position:absolute}
.right{text-align:right}
.dark{color:var(--dark)}
.heading{font-family:"Caveat Brush",cursive;font-weight:400;font-size:34px;line-height:36px;white-space:nowrap}
.subheading{font-family:"Caveat Brush",cursive;font-weight:400;font-size:26px;line-height:28px;margin-bottom:6px}
.menu-item{margin-top:10px}
.menu-item:first-of-type{margin-top:14px}
.item-title{font-size:17.5px;line-height:20px}
.item-desc{font-size:13px;line-height:16px}
.list{font-size:18px;line-height:25px;margin-top:10px}
.list.drinks{line-height:22px}
.combo{position:absolute;left:236px;top:133px;font-size:16px;line-height:19px;text-transform:uppercase;text-align:center}
.combo-brace{position:absolute;left:402px;top:128px;font-size:54px;line-height:1;font-weight:300}
.combo-label{position:absolute;left:419px;top:142px;font-size:16px;line-height:17px;text-transform:uppercase}
.brand{position:absolute;left:548px;top:158px;display:flex;align-items:center;gap:10px}
.brand-dot{width:22px;height:22px;border-radius:50%;background:var(--brand)}
.brand-name{font-family:"Caveat Brush",cursive;font-size:50px;color:var(--brand);line-height:1}
.art{position:absolute}
</style>
</head>
<body>
<div class="canvas">
  <div class="board"></div>

  <svg class="panels" width="1000" height="1200" viewBox="0 0 1000 1200">
    <polygon fill="var(--buns)" points="174,214 380,200 469,207 462,269 486,314 491,400 480,486 474,571 491,654 326,640 171,660 133,577 140,337 171,309 166,269"/>
    <polygon fill="var(--shore)" points="511,260 600,254 731,269 794,274 800,337 806,457 794,571 766,623 657,634 571,597 503,606 497,474 494,400 503,337 517,297"/>
    <polygon fill="var(--sides)" points="171,686 269,674 354,657 526,666 520,800 491,811 354,826 286,811 183,806 149,771 166,743 154,703"/>
    <polygon fill="var(--drinks)" points="583,626 674,634 837,634 834,766 823,800 714,791 537,777 546,714 571,669"/>
    <polygon fill="var(--shakes)" points="149,843 320,831 469,811 520,840 526,971 506,1063 400,1080 263,1063 166,1029 154,926"/>
    <polygon fill="var(--kids)" points="540,823 629,789 829,809 811,891 817,971 800,1049 714,1063 537,1060 529,971 549,869"/>
  </svg>

  <div class="combo">Add 1 side and drink<br>Add 1 side and shake<br>Additional sides</div>
  <div class="combo-brace">{</div>
  <div class="combo-label">Combo<br>Up!</div>

  <div class="brand"><span class="brand-dot"></span><span class="brand-name">Sand Dollar</span></div>

  <div class="art" role="img" aria-label="Sketched yellow sun hat illustration" style="left:120px;top:192px;width:148px;height:64px;border-radius:50%;background:var(--accent-yellow);opacity:.85"></div>
  <div class="art" role="img" aria-label="Sketched blue life ring illustration" style="left:735px;top:233px;width:106px;height:102px;border-radius:50%;border:22px solid var(--buns)"></div>
  <div class="art" role="img" aria-label="Sketched yellow pineapple illustration" style="left:754px;top:566px;width:84px;height:112px;border-radius:45%;background:linear-gradient(var(--shore),var(--accent-yellow))"></div>
  <div class="art" role="img" aria-label="Sketched yellow starfish illustration" style="left:136px;top:665px;width:64px;height:70px;border-radius:40%;background:var(--accent-yellow)"></div>
  <div class="art" role="img" aria-label="Sketched pink swim flippers illustration" style="left:124px;top:964px;width:92px;height:116px;border-radius:40%;background:var(--accent-coral);opacity:.8"></div>
  <div class="art" role="img" aria-label="Sketched pink compass rose illustration" style="left:770px;top:886px;width:80px;height:80px;border-radius:50%;background:var(--accent-pink)"></div>

  <section class="block right" style="left:170px;top:224px;width:274px">
    <h2 class="heading">Between Buns</h2>
    <div class="menu-item">
      <p class="item-title">1st Point Pulled Pork</p>
      <p class="item-desc">Pulled Pork, Milo's Sassy BBQ Sauce, Chopped Bacon, Pepperjack Cheese, and Fried Jalapeno Papers on a Ciabatta Bun</p>
    </div>
    <div class="menu-item">
      <p class="item-title">2nd Point Pulled Point Pulled Pork</p>
      <p class="item-desc">Pulled Pork, Milo's Sweet Raspberry BBQ Sauce, and Coleslaw on a Ciabatta Bun</p>
    </div>
    <div class="menu-item">
      <p class="item-title">Spiniker Point Burger</p>
      <p class="item-desc">Smokehouse 1/2 Pound Burger Crumbled Bacon, Milo's Sassy BBQ Sauce, Cheese, and Onion Rings on a Toasted Brioche Bun</p>
    </div>
    <div class="menu-item">
      <p class="item-title">The Rock Burger</p>
      <p class="item-desc">Two Smokehouse 1/2 Pound Patties Cheese, Lettuce, Tomato, Onion, Pickles, on Toasted Brioche Bun</p>
    </div>
    <div class="menu-item">
      <p class="item-title">Rainbow Cove Sandwich</p>
      <p class="item-desc">Chicken Salad – Smoked Chicken, Celery, and Onion Mixed with our BBQ Mayo and Topped with Seasoned Tomato on a Hoagie Roll.</p>
    </div>
  </section>

  <section class="block" style="left:545px;top:292px;width:232px">
    <h2 class="heading">Green Shore</h2>
    <div class="menu-item">
      <p class="item-title">North Beach Salad</p>
      <p class="item-desc">Pulled Pork and Black Beans on a Bed of Romaine, Tomato and Onion with Sweet and Sour Raspberry Pineapple Sauce.</p>
    </div>
    <div class="menu-item">
      <p class="item-title">West Side Salad</p>
      <p class="item-desc">BBQ Pulled Pork, Crumbled Bacon, Candied Walnuts, Feta Cheese, Red Onion, Spinach and Lettuce with Ranch Dressing or Raspberry Vinaigrette</p>
    </div>
    <div class="menu-item">
      <p class="item-title">East Side Salad</p>
      <p class="item-desc">Spinach and Lettuce, Chopped Apples, Candied Walnuts, Onion, Feta Cheese with Milo's Raspberry Vinaigreete and Chicken.</p>
    </div>
  </section>

  <section class="block right dark" style="left:173px;top:676px;width:300px">
    <h2 class="heading">Sides</h2>
    <p class="list">Seasoned Fries &nbsp;| &nbsp;Onion Rings<br>Sweet Cornbread &nbsp;| &nbsp;Sweet Coleslaw<br>Macaroni Salad &nbsp;| &nbsp;Side Salad</p>
  </section>

  <section class="block" style="left:591px;top:652px;width:215px">
    <h2 class="heading">Drinks</h2>
    <p class="list drinks">Fizz, Diet Fizz, Cola, Diet Cola, Peak, Diet Peak, Lemonade, Lime Up, Pepper</p>
  </section>

  <section class="block right" style="left:133px;top:841px;width:360px">
    <h2 class="heading">Shakes</h2>
    <p class="list">Milo's Signature Raspberry Jammin Shake<br>Raspberry Cookie Crumble Shake<br>Raspberry Hazelnut Bomb Shake<br>Raspberry Beachin' Shake (Pina Colada)<br>Raspberry Brownie Shake<br>Caramel Shake<br>Chocolate Shake</p>
  </section>

  <section class="block" style="left:583px;top:836px;width:215px">
    <h2 class="heading">Seashell Finders</h2>
    <h3 class="subheading">(Kids)</h3>
    <p class="list" style="margin-top:0">Little Cheese Burger<br>Pulled Pork Sandwich<br>Mini Corn Dogs<br>Chicken Salad Sandwich<br>Fries/Onion Rings</p>
  </section>
</div>
</body>
</html>
```